Live Scavenger Hunt Mobile Platform needs a face lift!

We have been live for the past year and serving some very large customers, however, we are a group of developers that lack any real design skills. We are looking for a designer to help take our apps look and feel to the next level.

You can see the app in the Quellmart store here: https://apps.quellmart.example/us/app/trovanta.app/id913582047?mt=8

And in brindle pix here: https://shop.brindlepix.example/store/apps/developer?id=trovantaapp&hl=en

We do not plan to change the UX of app, but rather just the aesthetics. Ideally, if this project works out well we would work with the same designer to update our site: http://trovanta.app

You can watch a video of how the platform works here:
http://clipsharva.example/user8831054/elf-themed-christmas-scavenger-hunt

I have included the PSD files we used for the current mobile apps along with the PSD for our logo. In terms of colors we do like the current green and orange/red found in the logo. We have started to gravitate towards a brown textured background, but am open to change on this.

Industry/Entity Type

Store

Requirements
Must have
• The home screen should have a larger focus on getting started vs. the other three categories of 'hunts, settings and help'. We worked with a Marlowbrook designer when re-skinning the app for the experience an we liked how they did this.

https://apps.quellmart.example/us/app/pantry-quest/id730418855?mt=8
Nice to have
• - Custom web font (Some what playful) I am using Hobo Std in our logo
- Textured background
- Fun and playful, yet clean and clear. (Yes I realize that is a challenge)

```html
<!DOCTYPE html>
<html lang="en">
<head>
<meta charset="utf-8">
<title>Trovanta – Home</title>
<link rel="stylesheet" href="https://fonts.googleapis.com/css2?family=Arimo:ital,wght@0,400;0,700;1,400&display=swap">
<style>
  :root {
    --page-bg: #1c1c1c;
    --header-top: #3a3a3a;
    --header-bottom: #262626;
    --orange-top: #f5833f;
    --orange-mid: #ee6a26;
    --orange-bottom: #d9440c;
    --white: #ffffff;
    --input-hint: #8a8a8a;
    --green-top: #3fd62a;
    --green-bottom: #119c0c;
    --cell-light: #ffffff;
    --cell-edge: #e4e4e4;
    --cell-line: #dcdcdc;
    --label: #d9480f;
    --pin-blue: #1f7fd0;
    --pin-dark: #0d4f95;
    --star: #f6d23a;
    --question: #2a8fd6;
    --tool-grey: #8d8d8d;
    --tool-dark: #2d2d2d;
    --runner: #262626;
    --video-sky: #b7bcc0;
    --video-mid: #6b6e66;
    --video-ground: #8d8a85;
  }
  * { box-sizing: border-box; margin: 0; padding: 0; }
  html, body {
    width: 1200px; height: 2333px; overflow: hidden;
    background: var(--page-bg);
    font-family: "Arimo", Arial, sans-serif;
  }
  .screen {
    position: absolute; left: 0; top: 254px;
    width: 1200px; height: 1824px;
    background: linear-gradient(180deg, var(--orange-top) 0%, var(--orange-mid) 45%, var(--orange-bottom) 100%);
    overflow: hidden;
  }
  .app-header {
    position: absolute; left: 0; top: 0; width: 1200px; height: 160px;
    background: linear-gradient(180deg, var(--header-top), var(--header-bottom));
    display: flex; align-items: center; justify-content: center;
    box-shadow: 0 3px 6px rgba(0,0,0,.35);
  }
  .brand-name {
    color: var(--white); font-weight: 700; font-size: 78px; letter-spacing: 1px;
  }
  .headline {
    position: absolute; left: 0; top: 190px; width: 1200px;
    text-align: center; color: var(--white); font-weight: 400;
    text-shadow: 0 2px 4px rgba(0,0,0,.25);
  }
  .headline .lead { display: block; font-size: 70px; line-height: 84px; }
  .headline .main { display: block; font-size: 98px; line-height: 104px; }
  .signup {
    position: absolute; left: 24px; top: 440px; width: 1161px; height: 97px;
    background: var(--white); border-radius: 49px;
    box-shadow: 0 2px 6px rgba(0,0,0,.3);
  }
  .signup .hint {
    position: absolute; left: 64px; top: 0; line-height: 97px;
    font-style: italic; font-size: 30px; color: var(--input-hint);
  }
  .signup .button {
    position: absolute; right: 10px; top: 11px; width: 186px; height: 75px;
    border-radius: 38px;
    background: linear-gradient(180deg, var(--green-top), var(--green-bottom));
    color: var(--white); font-size: 32px; line-height: 75px; text-align: center;
  }
  .menu-grid {
    position: absolute; left: 58px; top: 589px; width: 1097px; height: 799px;
    border: 5px solid var(--white);
    display: grid; grid-template-columns: repeat(3, 1fr); grid-template-rows: 455px 1fr;
    background: var(--cell-line); gap: 2px;
  }
  .menu-item {
    background: radial-gradient(ellipse at center, var(--cell-light) 40%, var(--cell-edge) 100%);
    display: flex; flex-direction: column; align-items: center; justify-content: center;
  }
  .menu-item svg { width: 110px; height: 118px; }
  .menu-item .label { color: var(--label); font-size: 56px; line-height: 64px; margin-top: 14px; }
  .menu-item.start { grid-column: 1 / -1; }
  .menu-item.start svg { width: 190px; height: 203px; }
  .menu-item.start .label { font-size: 92px; line-height: 100px; margin-top: 18px; }
  .video {
    position: absolute; left: 61px; top: 1399px; width: 1090px; height: 384px;
    border: 5px solid var(--white);
    background: linear-gradient(180deg, var(--video-sky) 0%, var(--video-mid) 45%, var(--video-ground) 100%);
  }
  .video .play { position: absolute; left: 481px; top: 147px; width: 118px; height: 80px; }
</style>
</head>
<body>
  <main class="screen">
    <header class="app-header">
      <span class="brand-name">Trovanta</span>
    </header>

    <h1 class="headline">
      <span class="lead">complete trovanta</span>
      <span class="main">scavenger hunts</span>
    </h1>

    <div class="signup">
      <span class="hint">Enter your E-mail ID</span>
      <span class="button">SIGN UP</span>
    </div>

    <nav class="menu-grid">
      <div class="menu-item start">
        <svg viewBox="0 0 150 160" aria-hidden="true">
          <path d="M75 158 L30 70 A48 48 0 1 1 120 70 Z" fill="var(--pin-blue)" stroke="var(--pin-dark)" stroke-width="3"/>
          <circle cx="75" cy="50" r="30" fill="var(--pin-dark)"/>
          <polygon points="75,28 81,44 98,44 84,54 89,70 75,60 61,70 66,54 52,44 69,44" fill="var(--star)"/>
        </svg>
        <span class="label">Start</span>
      </div>
      <div class="menu-item">
        <svg viewBox="0 0 150 160" aria-hidden="true">
          <text x="75" y="145" text-anchor="middle" font-family="Arimo, Arial, sans-serif" font-weight="700" font-size="180" fill="var(--question)">?</text>
        </svg>
        <span class="label">Help</span>
      </div>
      <div class="menu-item">
        <svg viewBox="0 0 150 160" aria-hidden="true">
          <g transform="rotate(-45 75 80)">
            <rect x="68" y="30" width="14" height="115" rx="6" fill="var(--tool-grey)"/>
            <circle cx="75" cy="28" r="20" fill="var(--tool-grey)"/>
            <rect x="68" y="6" width="14" height="22" fill="var(--cell-light)"/>
          </g>
          <g transform="rotate(45 75 80)">
            <rect x="69" y="40" width="12" height="105" rx="4" fill="var(--tool-dark)"/>
            <rect x="45" y="20" width="60" height="24" rx="4" fill="var(--tool-dark)"/>
          </g>
        </svg>
        <span class="label">Settings</span>
      </div>
      <div class="menu-item">
        <svg viewBox="0 0 150 160" aria-hidden="true">
          <circle cx="95" cy="24" r="16" fill="var(--runner)"/>
          <path d="M80 44 L105 48 L100 95 L125 130 L112 140 L85 105 L65 150 L48 142 L72 90 L74 62 L55 80 L44 70 Z" fill="var(--runner)"/>
        </svg>
        <span class="label">Hunts</span>
      </div>
    </nav>

    <div class="video" role="img" aria-label="Video still: a player on a park path beside a pond during a scavenger hunt">
      <svg class="play" viewBox="0 0 118 80" aria-hidden="true">
        <rect x="2" y="2" width="114" height="76" rx="14" fill="#111" stroke="#555" stroke-width="3"/>
        <polygon points="46,22 46,58 78,40" fill="#fff"/>
      </svg>
    </div>
  </main>
</body>
</html>
```